Coastal Body Remedies business is seeking a Business Card Design

We are a new natural therapy business that needs a Business Card Design with an appointment card on the back.

We offer Myotherapy (muscle therapy) services and have a strong focus and commitment to helping people relieve pain and restore movement to their bodies.

I am attaching my business logo for you information.

Business card must contain my logo and have space for name, title, qualifications, phone number, email, web address

Appointment Card on the back of the card must contain space to write next appointment date, time and name of therapist and cancellation policy.

Cancellation Policy
Minimum of 24hrs notice is required prior to appointment time or full treatment fees with apply.

```html
<!DOCTYPE html>
<html lang="en">
<head>
<meta charset="utf-8">
<title>Coastal Body Remedies – Business Card</title>
<link href="https://fonts.googleapis.com/css2?family=Open+Sans:wght@400;600;700&display=swap" rel="stylesheet">
<style>
  :root{
    --bg:#ece8e3;
    --card-white:#ffffff;
    --brand-red:#c11f31;
    --brand-brown:#4f4541;
    --brand-green:#7ab648;
    --ink:#333333;
    --ink-soft:#555555;
    --rule:#b9b9b9;
  }
  *{box-sizing:border-box;margin:0;padding:0}
  html,body{width:1200px;height:1019px;overflow:hidden;background:var(--bg)}
  body{position:relative;font-family:"Open Sans",Arial,sans-serif;color:var(--ink)}

  .card{position:absolute;left:320px;width:560px;height:320px;overflow:hidden;
        box-shadow:0 6px 18px rgba(0,0,0,.18)}
  .card--front{top:150px;background:var(--card-white)}
  .card--back{top:540px;background:var(--brand-red)}
  .card__art{position:absolute;inset:0}

  .brand{position:absolute;left:38px;top:176px;display:flex;align-items:center;gap:10px}
  .brand__mark{width:28px;height:28px;background:var(--brand-red);flex:none}
  .brand__name{font-weight:700;font-size:17px;color:var(--brand-red);white-space:nowrap}

  .contact{position:absolute;left:292px;top:26px}
  .contact__name{font-weight:700;font-size:17px;line-height:1.3;color:var(--ink)}
  .contact__title{font-size:12px;line-height:1.4;color:var(--brand-green);margin-bottom:10px}
  .contact__address{font-weight:700;font-size:11px;line-height:1.45;color:var(--ink);margin-bottom:6px}
  .contact__line{display:flex;align-items:center;gap:8px;font-size:11px;line-height:1.6;color:var(--ink-soft);white-space:nowrap}
  .contact__icon{width:11px;height:11px;flex:none}

  .appointment{position:absolute;left:300px;top:0;width:210px;height:320px;
               padding:34px 18px 0;background:linear-gradient(90deg,#f1f1f1,#ffffff)}
  .appointment__heading{font-weight:700;font-size:14px;color:var(--brand-red);margin-bottom:18px}
  .appointment__field{display:flex;align-items:flex-end;gap:8px;font-size:11px;font-weight:600;
                      color:var(--ink);margin-bottom:20px}
  .appointment__blank{flex:1;border-bottom:1px solid var(--rule);height:14px}
  .appointment__policy{margin-top:26px;font-size:9px;line-height:1.5;color:var(--ink-soft)}
  .appointment__policy strong{display:block;color:var(--ink);font-size:9.5px;margin-bottom:2px}
</style>
</head>
<body>

<section class="card card--front">
  <svg class="card__art" viewBox="0 0 560 320" aria-hidden="true">
    <path d="M0 255 C260 320 500 270 560 60 L560 320 L0 320 Z" fill="var(--brand-red)"/>
    <path d="M372 234 C470 190 525 140 552 30" fill="none" stroke="var(--brand-brown)" stroke-width="6"/>
    <path d="M20 272 C200 305 370 290 470 235" fill="none" stroke="#ffffff" stroke-opacity=".55" stroke-width="2"/>
  </svg>

  <div class="brand">
    <span class="brand__mark"></span>
    <span class="brand__name">Coastal Body Remedies</span>
  </div>

  <div class="contact">
    <p class="contact__name">Daniel Hartley</p>
    <p class="contact__title">President &amp; CEO</p>
    <p class="contact__address">12 Harbour Lane, Suite 4<br>Seacliff Bay SCB</p>
    <p class="contact__line">
      <svg class="contact__icon" viewBox="0 0 12 12"><path d="M2 1h3l1 3-2 1a7 7 0 0 0 3 3l1-2 3 1v3c-6 0-10-4-10-9z" fill="var(--brand-green)"/></svg>
      (012) 555 0142
    </p>
    <p class="contact__line">
      <svg class="contact__icon" viewBox="0 0 12 12"><rect x="3" y="0.5" width="6" height="11" rx="1" fill="none" stroke="var(--brand-green)" stroke-width="1.4"/></svg>
      (012) 555 0142
    </p>
    <p class="contact__line">
      <svg class="contact__icon" viewBox="0 0 12 12"><rect x="1" y="4" width="10" height="7" fill="var(--brand-green)"/><rect x="3" y="1" width="6" height="4" fill="var(--brand-green)"/></svg>
      (012) 555 0142
    </p>
    <p class="contact__line">
      <svg class="contact__icon" viewBox="0 0 12 12"><rect x="0.5" y="2" width="11" height="8" fill="var(--brand-green)"/><path d="M1 2.5 6 7l5-4.5" fill="none" stroke="#fff" stroke-width="1"/></svg>
      hello@coastalbody.com
    </p>
  </div>
</section>

<section class="card card--back">
  <div class="appointment">
    <p class="appointment__heading">Next Appointment</p>
    <p class="appointment__field">Date <span class="appointment__blank"></span></p>
    <p class="appointment__field">Time <span class="appointment__blank"></span></p>
    <p class="appointment__field">Therapist <span class="appointment__blank"></span></p>
    <p class="appointment__policy"><strong>Cancellation Policy</strong>Minimum of 24hrs notice is required prior to appointment time or full treatment fees will apply.</p>
  </div>
</section>

</body>
</html>
```